Miles Corbett Optometry 10 Year Celebration

Front of invitation
Size 107-139mm
Font – Georgia
The invitation should be worded as follows;
Miles Corbett Optometry
would like to invite you to...

```html
<!DOCTYPE html>
<html lang="en">
<head>
<meta charset="utf-8">
<title>Miles Corbett Optometry – 10 Year Celebration Invitation</title>
<link href="https://fonts.googleapis.com/css2?family=Damion&family=Gelasio:wght@400;700&display=swap" rel="stylesheet">
<style>
  :root{
    --stage:#0a0d18;
    --plum:#573359;
    --plum-deep:#3f2442;
    --paper:#ffffff;
    --gold:#e2bf3a;
    --gold-light:#f0dc7c;
    --sun:#f3d96b;
    --ink:#2b1f2d;
    --ink-soft:#3a2f33;
  }
  *{box-sizing:border-box;margin:0;padding:0}
  html,body{width:1200px;height:1181px;overflow:hidden;background:var(--stage)}
  body{position:relative;font-family:Georgia,"Gelasio",serif;color:var(--ink)}

  .card{position:absolute;top:35px;width:524px;height:1110px;overflow:hidden;background:var(--paper)}
  .card--front{left:57px}
  .card--back{left:623px}

  /* front stripes */
  .stripe{position:absolute;left:0;width:100%;height:124px;background:var(--plum)}
  .confetti{position:absolute}
  .card--front .confetti{left:0;top:160px;width:524px;height:800px;
    background:radial-gradient(ellipse 50% 50% at 50% 50%,rgba(226,191,58,.55) 0%,rgba(226,191,58,.3) 55%,rgba(226,191,58,0) 75%)}

  .badge{position:absolute;left:39px;top:335px;width:444px;height:444px;border-radius:50%;
    background:var(--sun);box-shadow:0 10px 22px rgba(40,20,40,.35);text-align:center;color:var(--ink-soft)}
  .badge__host{position:absolute;top:60px;width:100%;font-weight:700;font-size:23px}
  .badge__lead{position:absolute;top:90px;width:100%;font-size:21px}
  .badge__word{position:absolute;left:-20px;top:140px;width:484px;height:170px;overflow:visible}
  .badge__word text{font-family:"Damion",cursive;font-size:128px;fill:var(--plum);
    stroke:var(--paper);stroke-width:10px;paint-order:stroke;stroke-linejoin:round}
  .badge__occasion{position:absolute;top:296px;width:100%;font-size:25px}
  .badge__venue{position:absolute;top:324px;width:100%;font-size:30px}
  .badge__details{position:absolute;top:358px;width:100%;font-size:17px;line-height:21px}

  .footer{position:absolute;left:0;bottom:0;width:100%;background:var(--plum);color:var(--paper);text-align:center}
  .card--front .footer{height:121px;display:flex;align-items:center;justify-content:center}
  .brand{display:flex;align-items:center;gap:12px;font-size:27px;font-family:Georgia,"Gelasio",serif}
  .brand__dot{width:14px;height:14px;border-radius:50%;background:currentColor}

  /* back */
  .gold-band{position:absolute;left:0;width:100%;height:22px;
    background:linear-gradient(180deg,var(--gold-light) 0 30%,var(--gold) 30% 75%,var(--gold-light) 75%)}
  .card--back .gold-band--top{top:0}
  .card--back .gold-band--bottom{top:975px}
  .card--back .confetti{left:0;top:20px;width:524px;height:420px;
    background:linear-gradient(180deg,var(--plum) 0%,#8d6f8f 45%,rgba(255,255,255,0) 100%)}
  .headline{position:absolute;left:0;top:155px;width:100%;text-align:center;
    font-weight:700;font-size:47px;line-height:59px;color:var(--ink)}
  .message{position:absolute;left:0;top:463px;width:100%;text-align:center;font-size:21px;line-height:27px;color:var(--ink-soft)}
  .message p+p{margin-top:27px}
  .card--back .brand{position:absolute;top:850px;left:0;width:100%;justify-content:center;color:var(--ink);font-size:29px}
  .card--back .footer{height:112px;padding-top:24px;font-size:23px;line-height:28px}
  .contact{display:flex;align-items:center;justify-content:center;gap:7px}
  .contact svg{width:14px;height:14px;fill:var(--paper)}
</style>
</head>
<body>

<section class="card card--front" aria-label="Invitation front">
  <div class="stripe" style="top:0"></div>
  <div class="stripe" style="top:248px"></div>
  <div class="stripe" style="top:496px"></div>
  <div class="stripe" style="top:744px"></div>
  <div class="confetti" role="img" aria-label="Burst of gold confetti scattered around the badge"></div>

  <div class="badge">
    <p class="badge__host">Miles Corbett Optometry</p>
    <p class="badge__lead">would like to invite you to help us</p>
    <svg class="badge__word" viewBox="0 0 484 170" aria-label="Celebrate">
      <text x="242" y="130" text-anchor="middle">Celebrate</text>
    </svg>
    <p class="badge__occasion">our 10 year anniversary!</p>
    <p class="badge__venue">In our new location</p>
    <p class="badge__details">14 Carrow Street Elmsbury NSW<br>Tuesday 12th December<br>11:00 am – 7:00 pm</p>
  </div>

  <footer class="footer">
    <div class="brand"><span class="brand__dot"></span><span>Miles Corbett Optometry</span></div>
  </footer>
</section>

<section class="card card--back" aria-label="Invitation back">
  <div class="gold-band gold-band--top"></div>
  <div class="confetti" role="img" aria-label="Gold confetti falling over a plum to white fade"></div>
  <h1 class="headline">You are personally<br>invited to come and<br>experience our<br>brand new store!</h1>
  <div class="message">
    <p>Be one of the first to come in, with a chance to<br>try some new frames!<br>Special guests include a colour consultant &amp; brand<br>representatives. Refreshments &amp; nibbles provided.<br>Champagne into the evening.</p>
    <p>We would love the opportunity to celebrate with<br>our local community so bring along your<br>friends &amp; family!</p>
  </div>
  <div class="brand"><span class="brand__dot"></span><span>Miles Corbett Optometry</span></div>
  <div class="gold-band gold-band--bottom"></div>
  <footer class="footer">
    <p class="contact"><svg viewBox="0 0 24 24" aria-hidden="true"><path d="M12 1a8 8 0 0 0-8 8c0 6 8 14 8 14s8-8 8-14a8 8 0 0 0-8-8zm0 11a3 3 0 1 1 0-6 3 3 0 0 1 0 6z"/></svg>14 Carrow Street Elmsbury NSW</p>
    <p class="contact"><svg viewBox="0 0 24 24" aria-hidden="true"><path d="M3 9c0-3 4-5 9-5s9 2 9 5l-4 1-1-3H8L7 10zM5 12h14l1 8H4zm7 2a2.5 2.5 0 1 0 0 5 2.5 2.5 0 0 0 0-5z"/></svg>(02) 5550 4821</p>
  </footer>
</section>

</body>
</html>
```